Home care support

Design a a great and dynamic website for a healthcare business. Our business will be involved in providing care at home for people with disability and the elderly. Below is a link that I found for a company offering similar services in the US. I am looking for something like this .
I have my files - the latest project in here in through through PixelNest
Sample site : https://pinegroveattendants.net/
Target Market(s)
people with disability and elderly seniors who need home care support
Industry/Entity Type
Health
Coding
Coded - Design and coding required
Number of Pages Required
5+ page
Requirements
Must have
- inspirational pictures and designed with the themed logo (files attached)
Nice to have
- This is my sample and should look like this : https://pinegroveattendants.net/

```html
<!DOCTYPE html>
<html lang="en">
<head>
<meta charset="utf-8">
<title>Corvale Healthcare – Home Care Support</title>
<link href="https://fonts.googleapis.com/css2?family=Raleway:wght@300;400;500;600;700&display=swap" rel="stylesheet">
<style>
:root{
  --green:#6a9f3a;
  --green-dark:#5b8c2f;
  --blue:#0e68ad;
  --sky:#29a6de;
  --sky-light:#7fcbec;
  --pale:#eef6fa;
  --pale-2:#f3f8fb;
  --text:#555c63;
  --muted:#7b8288;
  --card-line:#bfe0ef;
  --white:#ffffff;
}
*{margin:0;padding:0;box-sizing:border-box}
html,body{width:1200px;height:4478px;overflow:hidden}
body{position:relative;font-family:"Raleway",sans-serif;color:var(--text);background:var(--white)}
.abs{position:absolute}
a{color:inherit;text-decoration:none}

/* header */
.topbar{left:670px;top:0;width:530px;height:31px;background:var(--green);clip-path:polygon(22px 0,100% 0,100% 100%,40px 100%);color:#fff;font-size:13px;display:flex;align-items:center;gap:34px;padding-left:74px}
.topbar span{display:flex;align-items:center;gap:7px}
.brand{left:122px;top:20px;display:flex;align-items:center;gap:10px}
.brand-dot{width:58px;height:58px;border-radius:50%;background:var(--blue)}
.brand-name{font-size:30px;font-weight:700;color:var(--blue);letter-spacing:1px}
.nav{left:426px;top:58px;display:flex;gap:58px;font-size:13px;font-weight:500;color:#333}
.nav a.active{color:var(--blue);font-weight:700;position:relative}
.nav a.active::after{content:"";position:absolute;left:-4px;right:-4px;top:30px;height:4px;background:var(--blue)}

/* hero */
.hero{left:0;top:101px;width:1200px;height:595px;background:var(--pale)}
.hero-arc{left:585px;top:101px;width:700px;height:595px;border-radius:110px 0 0 0;background:var(--sky-light)}
.hero-photo{left:617px;top:101px;width:583px;height:595px;border-radius:90px 0 0 0;background:linear-gradient(135deg,#e9c78a,#d6a36f 40%,#4d78a8 70%,#2c4f7f)}
.hero-copy{left:121px;top:262px;width:470px}
.h-light{font-size:36px;font-weight:400;color:var(--green);line-height:1.2}
.h-bold{font-size:36px;font-weight:600;color:var(--blue);line-height:1.3}
.hero-copy p{font-size:14px;line-height:24px;margin-top:16px;color:var(--text)}
.hero-info{margin-top:18px;font-size:15px;font-weight:600;color:var(--green)}
.hero-info b{color:var(--blue);font-size:19px;font-weight:700}
.btn{display:inline-flex;align-items:center;justify-content:center;border-radius:30px;font-size:13px;font-weight:700;text-transform:uppercase}
.btn-solid{background:var(--sky);color:#fff}
.btn-line{border:2px solid #fff;color:#fff}
.hero-btn{left:116px;top:485px;width:237px;height:54px}

/* about */
.about-ring{left:121px;top:787px;width:450px;height:440px;border-radius:50%;border:12px solid var(--sky-light);border-top-color:transparent;border-left-color:var(--sky-light)}
.about-photo{left:140px;top:788px;width:414px;height:414px;border-radius:50%;background:linear-gradient(135deg,#c9b5a1,#e8ddd0 45%,#8e9fb7)}
.about-copy{left:622px;top:816px;width:450px}
.sec-title{font-size:38px;font-weight:400;color:var(--green)}
.sec-title b{font-weight:700;color:var(--blue)}
.rule{width:70px;height:3px;background:var(--blue);margin-top:8px}
.about-copy p{font-size:14px;line-height:24px;margin-top:22px}
.feature{width:230px;display:flex;gap:12px}
.feature svg{flex:none}
.feature h4{font-size:14px;font-weight:600;color:var(--blue)}
.feature p{font-size:11px;line-height:16px;color:var(--muted);margin-top:4px}

/* blue band */
.band{left:0;top:1305px;width:1200px;height:542px;background:linear-gradient(90deg,#0a6eb5 0%,#1d8fd4 45%,#a9d5ee 62%,#ffffff 75%)}
.band-photo{left:560px;top:1305px;width:630px;height:542px;border-radius:0 320px 320px 0;background:linear-gradient(120deg,#d9e7ee,#6ea3cf 40%,#e7a7a4 70%,#6a7a56)}
.band-copy{left:133px;top:1416px;width:430px;color:#fff}
.band-copy h2{font-size:33px;font-weight:400;line-height:36px}
.band-copy p{font-size:14px;line-height:24px;margin-top:26px}
.band-btn{left:130px;top:1691px;width:168px;height:46px}

/* services */
.services-title{left:0;top:1918px;width:1200px;text-align:center}
.services-title .rule{margin:8px auto 0}
.card{width:238px;height:195px;border:2px solid var(--card-line);background:#fff;text-align:center;padding-top:28px}
.card.feat{background:var(--green);border-color:var(--green)}
.card h4{font-size:15px;font-weight:600;color:var(--blue);margin-top:14px}
.card p{font-size:10px;line-height:15px;color:var(--muted);margin:6px auto 0;width:180px}
.card.feat h4,.card.feat p{color:#fff}

/* approach */
.approach{left:0;top:2504px;width:1200px;height:522px;background:var(--pale-2);border-radius:0 200px 0 200px}
.approach-photo{left:129px;top:2588px;width:450px;height:369px;border-radius:0 60px 0 60px;background:linear-gradient(120deg,#d8d4cc,#a9b8a5 45%,#f2efe9 65%,#2c3550)}
.approach-copy{left:637px;top:2594px;width:430px}
.approach-copy h2{font-size:26px;line-height:36px;margin-top:14px}
.approach-copy .l{font-weight:400;color:var(--green)}
.approach-copy .b{font-weight:700;color:var(--blue)}
.approach-copy .rule{width:56px;margin-top:10px}
.approach-copy p{font-size:14px;line-height:24px;margin-top:18px}
.approach-btn{left:630px;top:2892px;width:168px;height:46px}

/* testimonials */
.say-title{left:0;top:3086px;width:1200px;text-align:center}
.say-title .rule{margin:8px auto 0}
.quote{width:420px;height:230px;border:2px solid var(--card-line);background:#fff;text-align:center;padding:56px 36px 0}
.quote p{font-size:14px;line-height:24px;color:#444}
.quote h5{font-size:14px;font-weight:600;color:#333;margin-top:10px}
.avatar{width:92px;height:92px;border-radius:50%;border:4px solid var(--green);background:linear-gradient(135deg,#c9c4bc,#8a8f96)}
.dots{left:558px;top:3481px;display:flex;gap:8px}
.dots i{width:14px;height:14px;border-radius:50%;border:1.5px solid #666;display:block}
.dots i.on{background:var(--sky);border-color:var(--sky)}

/* booking */
.book{left:0;top:3557px;width:1200px;height:573px;background:linear-gradient(90deg,#6a9f3a 0%,#6a9f3a 30%,#a3a46b 48%,#c8a987 62%,#c7c1b6 80%,#7b8f63 100%)}
.book-title{left:137px;top:3674px;font-size:33px;color:#fff;font-weight:400}
.book-title b{font-weight:700}
.field{left:136px;width:396px;height:43px;background:#fff;font-size:12px;color:#555;padding:14px 18px}
.book-btn{left:136px;top:4004px;width:167px;height:46px}

/* footer */
.foot-brand{left:148px;top:4225px;display:flex;align-items:center;gap:10px}
.foot-col{top:4200px;font-size:13px}
.foot-col h4{font-size:15px;font-weight:700;color:var(--blue);text-transform:uppercase}
.foot-col h4::after{content:"";display:block;width:30px;height:2px;background:var(--blue);margin-top:4px}
.foot-col li{list-style:none;color:#666;margin-top:10px}
.contact-row{display:flex;align-items:center;gap:8px;margin-top:16px;font-weight:500;color:#444}
.contact-row i{width:26px;height:26px;border-radius:50%;background:var(--sky);display:flex;align-items:center;justify-content:center}
.copyright{left:0;top:4426px;width:1200px;height:52px;background:var(--pale);font-size:12px;color:#777;text-align:center;line-height:52px}
</style>
</head>
<body>

<!-- header -->
<div class="abs topbar">
  <span><svg width="14" height="14" viewBox="0 0 24 24" fill="#fff"><path d="M6.6 10.8a15 15 0 006.6 6.6l2.2-2.2a1 1 0 011-.25 11 11 0 003.6.6 1 1 0 011 1V20a1 1 0 01-1 1A17 17 0 013 4a1 1 0 011-1h3.5a1 1 0 011 1 11 11 0 00.6 3.6 1 1 0 01-.25 1z"/></svg>(+555) 284 3106</span>
  <span><svg width="16" height="12" viewBox="0 0 16 12" fill="none" stroke="#fff" stroke-width="1.4"><rect x="1" y="1" width="14" height="10"/><path d="M1 1l7 6 7-6"/></svg>enquiry@corvalecare.com</span>
</div>
<div class="abs brand"><span class="brand-dot"></span><span class="brand-name">CORVALE</span></div>
<nav class="abs nav">
  <a class="active" href="#">HOME</a><a href="#">ABOUT US</a><a href="#">SERVICES</a><a href="#">RESOURCE</a><a href="#">BLOGS</a><a href="#">CONTACT</a>
</nav>

<!-- hero -->
<div class="abs hero"></div>
<div class="abs hero-arc"></div>
<div class="abs hero-photo" role="img" aria-label="Smiling nurse embracing an elderly man in a wheelchair outdoors"></div>
<div class="abs hero-copy">
  <div class="h-light">WELCOME TO</div>
  <div class="h-bold">CORVALE HEALTHCARE</div>
  <p>Lorem ipsum dolor sit amet, consectetur adipiscing elit,<br>sed do eiusmod tempor incididunt ut labore</p>
  <div class="hero-info">For more Information: <b>Call Us (555) 284 3106</b></div>
</div>
<a class="abs btn btn-solid hero-btn" href="#">Make an appointment</a>

<!-- about -->
<div class="abs about-ring"></div>
<div class="abs about-photo" role="img" aria-label="Caregiver combing an elderly woman's hair"></div>
<div class="abs about-copy">
  <h2 class="sec-title">ABOUT <b>CORVALE</b></h2>
  <div class="rule"></div>
  <p>Lorem ipsum dolor sit amet, consectetur adipiscing elit, sed do eiusmod tempor incididunt ut labore et dolore magna aliqua. Ut enim ad minim veniam, quis nostrud exercitation</p>
</div>
<div class="abs feature" style="left:617px;top:1012px">
  <svg width="40" height="46" viewBox="0 0 40 46" fill="none" stroke="var(--green)" stroke-width="2"><circle cx="20" cy="14" r="8"/><path d="M6 44c0-10 6-16 14-16s14 6 14 16z"/></svg>
  <div><h4>Friendly Staff</h4><p>Lorem ipsum dolor sit amet,<br>consectetur adipiscin</p></div>
</div>
<div class="abs feature" style="left:862px;top:1012px">
  <svg width="44" height="40" viewBox="0 0 44 40" fill="none" stroke="var(--green)" stroke-width="2"><path d="M22 34L9 21a7 7 0 0110-10l3 3 3-3a7 7 0 0110 10z"/><path d="M2 20v12l8 6M42 20v12l-8 6"/></svg>
  <div><h4>Choice of Caregiver</h4><p>Lorem ipsum dolor sit amet,<br>consectetur adipiscin</p></div>
</div>
<div class="abs feature" style="left:617px;top:1118px">
  <svg width="40" height="46" viewBox="0 0 40 46" fill="none" stroke="var(--green)" stroke-width="2"><path d="M6 24a14 14 0 0128 0"/><rect x="3" y="24" width="7" height="13" rx="3"/><rect x="30" y="24" width="7" height="13" rx="3"/><path d="M34 37c0 5-6 6-12 6"/></svg>
  <div><h4>On Call 24/7</h4><p>Lorem ipsum dolor sit amet,<br>consectetur adipiscin</p></div>
</div>
<div class="abs feature" style="left:870px;top:1118px">
  <svg width="36" height="40" viewBox="0 0 36 40" fill="none" stroke="var(--green)" stroke-width="2"><path d="M10 38v-8a14 14 0 1118-4l4 6h-4v6h-6v4"/><circle cx="18" cy="16" r="5"/></svg>
  <div><h4>Peace of Mind</h4><p>Lorem ipsum dolor sit amet,<br>consectetur adipiscin</p></div>
</div>

<!-- blue band -->
<div class="abs band"></div>
<div class="abs band-photo" role="img" aria-label="Nurse in blue scrubs holding hands with a smiling elderly woman"></div>
<div class="abs band-copy">
  <h2>PROVIDE BEST HOME<br>CARE SERVICE</h2>
  <p>Lorem ipsum dolor sit amet, consectetur adipiscing elit, sed do eiusmod tempor incididunt ut labore et dolore magna aliqua. Ut enim ad minim veniam, quis nostru.<br>Sed ut perspiciatis unde omnis iste natus error sit voluptatem accusantium doloremque laudantium, totam rem aperiam, eaque ipsa quae ab illo inventore</p>
</div>
<a class="abs btn btn-line band-btn" href="#">Learn more</a>

<!-- services -->
<div class="abs services-title"><h2 class="sec-title">OUR <b>SERVICES</b></h2><div class="rule"></div></div>

<div class="abs card" style="left:122px;top:2017px">
  <svg width="44" height="44" viewBox="0 0 44 44" fill="none" stroke="var(--sky)" stroke-width="2"><path d="M4 20L22 5l18 15M9 16v24h26V16"/><rect x="16" y="24" width="12" height="10"/><path d="M22 24v10M16 29h12"/></svg>
  <h4>Light Housekeeping</h4><p>Sed ut persp iciatis unde omnis iste natus error sit voluptatem accus antium doloremque</p>
</div>
<div class="abs card feat" style="left:368px;top:2017px">
  <svg width="44" height="44" viewBox="0 0 44 44" fill="none" stroke="#fff" stroke-width="2"><circle cx="28" cy="16" r="10"/><circle cx="30" cy="14" r="3"/><path d="M21 23L6 38l4 4M11 33l4 4"/></svg>
  <h4>Transportation</h4><p>Sed ut persp iciatis unde omnis iste natus error sit voluptatem accus antium doloremque</p>
</div>
<div class="abs card" style="left:614px;top:2017px">
  <svg width="44" height="44" viewBox="0 0 44 44" fill="none" stroke="var(--sky)" stroke-width="2"><rect x="6" y="3" width="26" height="38"/><path d="M6 11h26"/><circle cx="19" cy="25" r="8"/><rect x="30" y="32" width="12" height="9"/></svg>
  <h4>Laundry &amp; Linens</h4><p>Sed ut persp iciatis unde omnis iste natus error sit voluptatem accus antium doloremque</p>
</div>
<div class="abs card" style="left:860px;top:2017px">
  <svg width="44" height="44" viewBox="0 0 44 44" fill="none" stroke="var(--sky)" stroke-width="2"><rect x="8" y="3" width="18" height="6"/><rect x="6" y="9" width="22" height="32" rx="3"/><path d="M17 19v12M11 25h12"/><circle cx="35" cy="33" r="7"/></svg>
  <h4>Medication Reminders</h4><p>Sed ut persp iciatis unde omnis iste natus error sit voluptatem accus antium doloremque</p>
</div>
<div class="abs card" style="left:122px;top:2226px">
  <svg width="44" height="44" viewBox="0 0 44 44" fill="none" stroke="var(--sky)" stroke-width="2"><circle cx="22" cy="22" r="19"/><circle cx="22" cy="22" r="12"/><path d="M16 16l12 12M28 16L16 28"/></svg>
  <h4>Meal Preparation</h4><p>Sed ut persp iciatis unde omnis iste natus error sit voluptatem accus antium doloremque</p>
</div>
<div class="abs card" style="left:368px;top:2226px">
  <svg width="44" height="44" viewBox="0 0 44 44" fill="none" stroke="var(--sky)" stroke-width="2"><path d="M15 28a11 11 0 1114 0v5H15z"/><path d="M16 38h12M18 42h8M22 2v-2M6 10l-3-2M38 10l3-2"/></svg>
  <h4>Stimulating Activities</h4><p>Sed ut persp iciatis unde omnis iste natus error sit voluptatem accus antium doloremque</p>
</div>
<div class="abs card" style="left:614px;top:2226px">
  <svg width="44" height="44" viewBox="0 0 44 44" fill="none" stroke="var(--sky)" stroke-width="2"><circle cx="9" cy="36" r="5"/><circle cx="21" cy="36" r="5"/><path d="M11 32L22 4M19 32L8 4"/><rect x="30" y="4" width="8" height="36" rx="2"/></svg>
  <h4>Hygiene Assistance</h4><p>Sed ut persp iciatis unde omnis iste natus error sit voluptatem accus antium doloremque</p>
</div>
<div class="abs card" style="left:860px;top:2226px">
  <svg width="48" height="44" viewBox="0 0 48 44" fill="none" stroke="var(--sky)" stroke-width="2"><path d="M3 22h42v6a10 10 0 01-10 10H13A10 10 0 013 28z"/><path d="M10 22V8a5 5 0 0110 0M12 38l-2 5M36 38l2 5"/><circle cx="30" cy="14" r="3"/><circle cx="38" cy="10" r="2"/></svg>
  <h4>Kitchen &amp; Bathroom</h4><p>Sed ut persp iciatis unde omnis iste natus error sit voluptatem accus antium doloremque</p>
</div>

<!-- approach -->
<div class="abs approach"></div>
<div class="abs approach-photo" role="img" aria-label="Caregiver helping an elderly woman in a wheelchair at home"></div>
<div class="abs approach-copy">
  <svg width="42" height="42" viewBox="0 0 42 42" fill="none" stroke="var(--sky)" stroke-width="2"><circle cx="21" cy="21" r="19"/><path d="M17 10h8v7h7v8h-7v7h-8v-7h-7v-8h7z"/></svg>
  <h2><span class="l">SIMPLE, AFFORDABLE</span><br><span class="b">APPROACH TO HOME CARE</span></h2>
  <div class="rule"></div>
  <p>Lorem ipsum dolor sit amet, consectetur adipiscing elit, sed do eiusmod tempor incididunt ut labore et dolore magna aliqua. Ut enim ad minim veniam, quis nostru.Lorem ipsum dolor sit amet, consectetur adipiscing elit, sed do eiusmod tempor incididunt ut labore et dolore magna aliqua.</p>
</div>
<a class="abs btn btn-solid approach-btn" href="#">Learn more</a>

<!-- testimonials -->
<div class="abs say-title"><h2 class="sec-title">WHAT <b>PEOPLE SAYS</b></h2><div class="rule"></div></div>
<div class="abs quote" style="left:160px;top:3214px">
  <p>“Sed ut perspiciatis unde omnis iste natus error sit voluptatem accusantium doloremque laudantium, totam rem aperiam, eaque ipsa quae ab illo inventore veritatis et quasi architecto ”</p>
  <h5>Mara Ellison</h5>
</div>
<div class="abs quote" style="left:603px;top:3214px">
  <p>“Sed ut perspiciatis unde omnis iste natus error sit voluptatem accusantium doloremque laudantium, totam rem aperiam, eaque ipsa quae ab illo inventore veritatis et quasi architecto ”</p>
  <h5>Mara Ellison</h5>
</div>
<div class="abs avatar" style="left:324px;top:3166px" role="img" aria-label="Portrait of an elderly client"></div>
<div class="abs avatar" style="left:767px;top:3166px" role="img" aria-label="Portrait of an elderly client"></div>
<div class="abs dots"><i></i><i class="on"></i><i></i></div>

<!-- booking -->
<div class="abs book" role="img" aria-label="Caregiver hugging an elderly woman outdoors, over a green panel"></div>
<h2 class="abs book-title">BOOK <b>APPOINTMENT</b></h2>
<div class="abs field" style="top:3722px">Name</div>
<div class="abs field" style="top:3775px">Email address</div>
<div class="abs field" style="top:3835px">Phone Number</div>
<div class="abs field" style="top:3888px;height:92px">Message</div>
<a class="abs btn btn-line book-btn" href="#">Book now</a>

<!-- footer -->
<div class="abs foot-brand"><span class="brand-dot" style="width:70px;height:70px"></span><span class="brand-name" style="font-size:34px">CORVALE</span></div>
<div class="abs foot-col" style="left:433px">
  <h4>Navigation</h4>
  <ul><li>About Us</li><li>Our Services</li><li>Blogs</li><li>Book appointment</li></ul>
</div>
<div class="abs foot-col" style="left:645px">
  <h4>Resources</h4>
  <ul><li>Privacy Policy</li><li>Testimonials</li><li>FAQ</li><li>Contact Us</li></ul>
</div>
<div class="abs foot-col" style="left:838px">
  <h4>Contact Us</h4>
  <div class="contact-row"><i><svg width="13" height="13" viewBox="0 0 24 24" fill="#fff"><path d="M6.6 10.8a15 15 0 006.6 6.6l2.2-2.2a1 1 0 011-.25 11 11 0 003.6.6 1 1 0 011 1V20a1 1 0 01-1 1A17 17 0 013 4a1 1 0 011-1h3.5a1 1 0 011 1 11 11 0 00.6 3.6 1 1 0 01-.25 1z"/></svg></i>Location: Larkfield, OR</div>
  <div class="contact-row"><i><svg width="12" height="14" viewBox="0 0 12 16" fill="#fff"><path d="M6 0a6 6 0 00-6 6c0 4.5 6 10 6 10s6-5.5 6-10a6 6 0 00-6-6zm0 8.5A2.5 2.5 0 116 3.5a2.5 2.5 0 010 5z"/></svg></i>Phone: 303-555-0142</div>
  <div style="margin-top:18px;color:#666">Locally Owned, Nationally supported</div>
</div>
<div class="abs copyright">© Copyright 2022 Corvale | All Right Reserved</div>

</body>
</html>
```